Harbor Dental, LLC business card project

Business card to be designed with current logo.
Dental office- please keep design of card that looks clean and professional.
Please include the following info:
Harbor Dental, LLC
Dr. Corinne Pelham
3187 Elmwood
Millbrook, PA 17921
555-392-7158
harbordental.office@quillmail.net
Updates
Hello everyone-
Project Deadline Extended
Reason: Just got back from overseas- will look at all designs and provide feedback. Thank you!
Project Deadline Extended
Reason: Polling my friends for the final selection-
thank you to all those that participated- so many talented designers!
Business

```html
<!DOCTYPE html>
<html lang="en">
<head>
<meta charset="utf-8">
<title>Harbor Dental, LLC — Business Card</title>
<link rel="stylesheet" href="https://fonts.googleapis.com/css2?family=Questrial&family=Cinzel:wght@700&display=swap">
<style>
  :root {
    --page-bg: #ffffff;
    --card-border: #6f6f6f;
    --divider: #d3d3d3;
    --brand-green: #689f43;
    --brand-dark: #5f9a3c;
    --accent-lime: #b3d236;
    --text-dark: #222222;
    --text-light: #ffffff;
  }
  * { box-sizing: border-box; margin: 0; padding: 0; }
  html, body {
    width: 1200px;
    height: 1000px;
    overflow: hidden;
    background: var(--page-bg);
    font-family: "Questrial", "Century Gothic", sans-serif;
    color: var(--text-dark);
  }
  .sheet { position: relative; width: 1200px; height: 1000px; }

  .card { position: absolute; left: 295px; width: 608px; height: 350px; }
  .card--front { top: 80px; border: 2px solid var(--card-border); background: var(--page-bg); }
  .card--back { top: 527px; height: 348px; background: var(--brand-green); }

  .brand {
    position: absolute;
    display: flex;
    align-items: center;
    gap: 18px;
    white-space: nowrap;
  }
  .brand__dot { width: 44px; height: 44px; border-radius: 50%; flex: none; }
  .brand__name { font-family: "Questrial", "Century Gothic", sans-serif; font-weight: 400; }

  .card--front .brand { left: 40px; top: 30px; }
  .card--front .brand__dot { background: var(--accent-lime); }
  .card--front .brand__name { font-size: 50px; color: var(--brand-dark); letter-spacing: -1px; }

  .divider {
    position: absolute;
    left: -5px; right: -6px;
    top: 121px;
    height: 6px;
    background: var(--divider);
  }

  .contact {
    position: absolute;
    right: 24px;
    top: 178px;
    text-align: right;
  }
  .contact__name {
    font-family: "Cinzel", Georgia, serif;
    font-weight: 700;
    font-size: 25px;
    color: var(--brand-dark);
    letter-spacing: 1px;
    margin-bottom: 22px;
  }
  .contact__line {
    font-size: 19px;
    line-height: 24px;
    color: var(--text-dark);
  }
  .contact__line--bullet::before {
    content: "";
    display: inline-block;
    width: 11px; height: 11px;
    border-radius: 50%;
    background: var(--accent-lime);
    margin-right: 14px;
    vertical-align: 1px;
  }

  .card--back .brand {
    left: 50%;
    top: 112px;
    transform: translateX(-50%);
    flex-direction: column;
    gap: 28px;
  }
  .card--back .brand__dot { width: 70px; height: 70px; background: var(--accent-lime); }
  .card--back .brand__name { font-size: 40px; color: var(--text-light); letter-spacing: -1px; }

  .label {
    position: absolute;
    left: 0; width: 1200px;
    text-align: center;
    font-size: 22px;
    color: var(--text-dark);
  }
  .label--front { top: 452px; }
  .label--back { top: 898px; }
</style>
</head>
<body>
<main class="sheet">
  <section class="card card--front" aria-label="Card front">
    <div class="brand">
      <span class="brand__dot"></span>
      <span class="brand__name">Harbor Dental, LLC</span>
    </div>
    <div class="divider"></div>
    <div class="contact">
      <p class="contact__name">Dr. Corinne Pelham</p>
      <p class="contact__line contact__line--bullet">3187 Elmwood</p>
      <p class="contact__line">Millbrook, PA 17921</p>
      <p class="contact__line contact__line--bullet">555-392-7158</p>
      <p class="contact__line contact__line--bullet">harbordental.office@quillmail.net</p>
    </div>
  </section>
  <p class="label label--front">front</p>

  <section class="card card--back" aria-label="Card back">
    <div class="brand">
      <span class="brand__dot"></span>
      <span class="brand__name">Harbor Dental, LLC</span>
    </div>
  </section>
  <p class="label label--back">back</p>
</main>
</body>
</html>
```